Billboard design for dentist that sees only children

I own a 12' x 25' digital billboard and I need help with billboard design. My wife is a general dentist that only sees children and is very passionate about giving them a quality dental experience . She has a great reputation in town. Obviously with a billboard there can't be a lot of reading. Maybe something that shows safety, love, experience and children. I am completely open to your ideas. In addition I have other businesses that also need billboard design so this could lead to more work. If you go to Maplecovedental.com under the about section you will find more information about the practice and our phone number. Attached is our logo which could be changed and content specs for the digital billboard. Happy Designing!!

Target Market(s)

Parents with children

Colors

Designer to choose colors to be used in the design.

Requirements
Must have
• Must attract attention and be nice to look at.
Nice to have
• Probably should have children in the picture ..... Maybe
Should not have
• If I see something I don't like I will let you know

```html
<!DOCTYPE html>
<html lang="en">
<head>
<meta charset="utf-8">
<title>Maple Cove Dental – Billboard</title>
<link rel="stylesheet" href="https://fonts.googleapis.com/css2?family=Roboto+Slab:wght@400;800&family=Roboto+Condensed:wght@700&display=swap">
<style>
  :root {
    --backdrop: #3d3e42;
    --board: #ffffff;
    --headline-blue: #0ea0dc;
    --brand-teal: #2a7468;
    --tagline-blue: #2f8fc4;
    --cta-green: #23bb66;
    --cta-text: #ffffff;
    --photo-skin: #efcfb6;
    --photo-hair: #c9895a;
    --photo-towel: #3aa6d8;
  }
  * { box-sizing: border-box; margin: 0; padding: 0; }
  html, body {
    width: 1200px;
    height: 1200px;
    overflow: hidden;
    background: var(--backdrop);
  }
  .billboard {
    position: absolute;
    left: 50px;
    top: 339px;
    width: 1100px;
    height: 522px;
    background: var(--board);
    overflow: hidden;
  }
  .brand {
    position: absolute;
    left: 68px;
    top: 38px;
    display: flex;
    align-items: center;
    gap: 14px;
  }
  .brand-dot {
    width: 40px;
    height: 40px;
    border-radius: 50%;
    background: var(--brand-teal);
  }
  .brand-name {
    font-family: "Roboto Slab", serif;
    font-weight: 400;
    font-size: 42px;
    color: var(--brand-teal);
    line-height: 1;
  }
  .tagline {
    position: absolute;
    left: 282px;
    top: 90px;
    font-family: "Roboto Slab", serif;
    font-size: 19px;
    color: var(--tagline-blue);
  }
  .headline {
    position: absolute;
    left: 66px;
    font-family: "Roboto Slab", serif;
    font-weight: 800;
    color: var(--headline-blue);
    line-height: 1;
    letter-spacing: -1px;
  }
  .headline-healthy { top: 150px; font-size: 94px; }
  .headline-smile   { top: 222px; font-size: 94px; }
  .headline-early   { top: 316px; font-size: 66px; letter-spacing: -0.5px; }
  .cta {
    position: absolute;
    left: 68px;
    top: 418px;
    width: 482px;
    height: 65px;
    background: var(--cta-green);
    display: flex;
    align-items: center;
    justify-content: center;
    gap: 18px;
    font-family: "Roboto Condensed", sans-serif;
    font-weight: 700;
    font-size: 40px;
    color: var(--cta-text);
  }
  .hero-photo {
    position: absolute;
    left: 660px;
    top: 50px;
    width: 440px;
    height: 472px;
    background:
      radial-gradient(ellipse 45% 35% at 52% 22%, var(--photo-hair), transparent 70%),
      radial-gradient(ellipse 38% 32% at 52% 45%, var(--photo-skin), transparent 75%),
      linear-gradient(180deg, #ffffff 0%, var(--photo-skin) 55%, var(--photo-towel) 100%);
  }
</style>
</head>
<body>
  <section class="billboard">
    <div class="brand">
      <span class="brand-dot"></span>
      <span class="brand-name">Maple Cove Dental</span>
    </div>
    <p class="tagline">general dentistry for children</p>

    <h1 class="headline headline-healthy">HEALTHY</h1>
    <p class="headline headline-smile">SMILE</p>
    <p class="headline headline-early">START EARLY</p>

    <div class="cta"><span>CALL</span><span>555-014-2290</span></div>

    <div class="hero-photo" role="img" aria-label="Smiling young child with a blue towel around the shoulders holding a colourful toothbrush"></div>
  </section>
</body>
</html>
```